Lumo Brew Premium Matcha brand Label

This is a label design project for a luxury tea brand. Feel free to be creative within the guidelines.
Attached to this project is a document called “Private Label Design Requirements” with the design guidelines and template. There is another document called "Lumo Brew Packaging Instructions" this has more details necessary to stick to the guidelines in the first document.

I have also attached the certifications to be included as well as different variations of the logo for you to use.

If you have any questions, I am here.
Updates

Target Market(s)

Young, active, fun, enjoy the finer things

```html
<!DOCTYPE html>
<html lang="en">
<head>
<meta charset="utf-8">
<title>Lumo Brew Premium Matcha Label</title>
<link href="https://fonts.googleapis.com/css2?family=Open+Sans:wght@400;600&display=swap" rel="stylesheet">
<style>
  :root {
    --bg-dark: #717276;
    --bg-mid: #8a8b8f;
    --bg-light: #b4b5b8;
    --text-white: #ffffff;
    --text-soft: #f1f1f1;
    --text-grey: #e6e6e6;
    --rule-blue: #2aa6df;
    --badge-ring: #6b3b22;
    --badge-fill: #1f7a44;
    --edge: #d9534f;
  }
  * { margin: 0; padding: 0; box-sizing: border-box; }
  html, body { width: 1200px; height: 234px; overflow: hidden; }
  body { font-family: "Open Sans", sans-serif; }
  .label {
    position: relative;
    width: 1200px;
    height: 234px;
    overflow: hidden;
    border: 1px solid var(--edge);
  }
  .backdrop {
    position: absolute;
    inset: 0;
    background:
      radial-gradient(ellipse 320px 200px at 600px 110px, var(--bg-light), transparent 75%),
      radial-gradient(ellipse 260px 140px at 230px 150px, rgba(150,110,90,0.35), transparent 70%),
      radial-gradient(ellipse 220px 140px at 1050px 150px, rgba(200,200,200,0.35), transparent 70%),
      linear-gradient(180deg, var(--bg-dark), var(--bg-mid));
  }
  .distributor {
    position: absolute;
    left: 74px;
    top: 88px;
    color: var(--text-white);
    font-size: 15.5px;
    line-height: 20.5px;
  }
  .brand {
    position: absolute;
    left: 0;
    width: 1200px;
    top: 38px;
    text-align: center;
    color: var(--text-white);
  }
  .brand-mark {
    display: block;
    margin: 0 auto 10px;
    width: 62px;
    height: 62px;
    border-radius: 50%;
    background: #6cc04a;
  }
  .brand-name { font-size: 24px; font-weight: 400; line-height: 28px; }
  .brand-sub { font-size: 13.5px; font-weight: 600; margin-top: 5px; }
  .net-weight { font-size: 19px; line-height: 24px; }
  .ingredients {
    position: absolute;
    left: 815px;
    top: 43px;
    color: var(--text-white);
  }
  .ingredients-title { font-size: 13px; font-weight: 600; line-height: 20px; }
  .ingredients-item { font-size: 13px; font-weight: 600; line-height: 20px; }
  .ingredients-rule {
    width: 85px;
    height: 1.5px;
    background: var(--rule-blue);
    margin: 6px 0 6px;
  }
  .steps { list-style: none; font-size: 11px; line-height: 14.6px; color: var(--text-soft); }
  .steps li::before { content: "• "; }
  .cert-badge {
    position: absolute;
    left: 947px;
    top: 146px;
    width: 41px;
    height: 41px;
    border-radius: 50%;
    background: var(--badge-fill);
    border: 2px solid var(--badge-ring);
    box-shadow: inset 0 0 0 3px #fff;
  }
  .storage {
    position: absolute;
    left: 1001px;
    top: 147px;
    color: var(--text-grey);
    font-size: 13px;
    font-weight: 600;
    line-height: 17.5px;
    letter-spacing: 0.2px;
  }
</style>
</head>
<body>
  <div class="label">
    <div class="backdrop" role="img" aria-label="Soft-focus photo of a clay teapot, matcha powder bowls, bamboo whisk and loose tea leaves on a wooden table"></div>

    <div class="distributor">
      <p>Distributed by Lumo Brew Co. | Savannah, Ga</p>
      <p>Certified Organic by Verda Cert</p>
      <p>PRODUCT OF JAPAN</p>
    </div>

    <div class="brand">
      <span class="brand-mark"></span>
      <p class="brand-name">Lumo Brew</p>
      <p class="brand-sub">Premium Organic Ceremonial Matcha</p>
      <p class="net-weight">Net Wt: 30g</p>
    </div>

    <div class="ingredients">
      <p class="ingredients-title">Ingredients</p>
      <p class="ingredients-item">Premium Organic Japanese Matcha Green Tea</p>
      <div class="ingredients-rule"></div>
      <ul class="steps">
        <li>2 tsp of Matcha</li>
        <li>2oz of Water (170-180 degrees F)</li>
        <li>Whisk in a W formation until frothy</li>
        <li>Sweeten to taste</li>
      </ul>
    </div>

    <div class="cert-badge" aria-hidden="true"></div>

    <div class="storage">
      <p>KEEP REFRIGERATED</p>
      <p>FOR QUALITY</p>
    </div>
  </div>
</body>
</html>
```